Business card for a plastic surgeon

i need a business card for a plastic surgeon. I have two adresses. The card should communicate safety, simmetry, beauty and with soft colors.
What i want in the card:
- my logo: Letters "R"and "B" (picture uploaded)
- my name: Renato Bastiani
- my registration: CRM 507 219
- my adresses and phone numbers (2):
- Av Dr Teixeira Lopes, 2710, sala 305 - Vila Olímpia | São Paulo/ SP - Phone: 11 4172-5036
- Al. Itapeva, 47, 3 andar - Alphaville | Barueri/ SP - Phone: 11 6350-2481

- my social network: www.renatobastiani.med.br, fb.com/drrenatobastiani and @dr.renatobastiani

Target Market(s)

people (95% girls and women) that want cosmetic procedures and plastic surgery

Industry/Entity Type

Business

Contact Information for Business Card

The card should communicate safety, simmetry, beauty and with soft colors.
Beige, brown, gray, rosy are some options. Color is free

Font styles to use
Serif

Requirements
Must have
• - my logo: Letters "R"and "B" (picture uploaded)
• - my name: Renato Bastiani
• - my registration: CRM 507 219
• - my adresses and phone numbers (2):
• - Av Dr Teixeira Lopes, 2710, sala 305 - Vila Olímpia | São Paulo/ SP - Phone: 11 4172-5036
• - Al. Itapeva, 47, 3 andar - Alphaville | Barueri/ SP - Phone: 11 6350-2481
• - my social network: www.renatobastiani.med.br, fb.com/drrenatobastiani and @dr.renatobastiani
Should not have
• other images (only my logo)

```html
<!DOCTYPE html>
<html lang="pt-BR">
<head>
<meta charset="UTF-8">
<title>Dr. Renato Bastiani — Cartão de Visita</title>
<link rel="stylesheet" href="https://fonts.googleapis.com/css2?family=Cinzel:wght@400;500&family=Tinos&display=swap">
<style>
  :root {
    --page-bg: #f1f0ee;
    --card-bg: #e7ddd5;
    --ink: #2b2522;
    --ink-soft: #4a403b;
    --taupe: #9a8272;
    --card-shadow: rgba(60, 45, 35, 0.18);
  }
  * { margin: 0; padding: 0; box-sizing: border-box; }
  html, body {
    width: 1200px;
    height: 1200px;
    overflow: hidden;
    background: var(--page-bg);
  }
  .sheet {
    width: 1200px;
    height: 1200px;
    display: flex;
    flex-direction: column;
    align-items: center;
    justify-content: center;
    gap: 60px;
  }
  .card {
    position: relative;
    width: 860px;
    height: 520px;
    background: var(--card-bg);
    box-shadow: 0 10px 30px var(--card-shadow);
  }
  .monogram {
    display: flex;
    align-items: center;
    gap: 14px;
    font-family: "Cinzel", serif;
    font-weight: 400;
    color: var(--taupe);
    letter-spacing: 0.08em;
  }
  .monogram-dot {
    width: 14px;
    height: 14px;
    border-radius: 50%;
    background: var(--taupe);
  }
  .doctor-name {
    font-family: "Cinzel", serif;
    font-weight: 500;
    color: var(--ink);
    letter-spacing: 0.02em;
    white-space: nowrap;
  }
  .specialty {
    font-family: "Cinzel", serif;
    font-weight: 400;
    color: var(--ink-soft);
    letter-spacing: 0.28em;
    white-space: nowrap;
  }

  /* Front */
  .card-front .front-mark {
    position: absolute;
    left: 0;
    right: 0;
    top: 120px;
    display: flex;
    flex-direction: column;
    align-items: center;
  }
  .card-front .monogram { font-size: 34px; margin-bottom: 70px; }
  .card-front .doctor-name { font-size: 50px; }
  .card-front .specialty { font-size: 24px; margin-top: 4px; }
  .social-line {
    position: absolute;
    left: 0;
    right: 0;
    bottom: 48px;
    display: flex;
    justify-content: center;
    gap: 26px;
    font-family: "Tinos", serif;
    font-style: normal;
    font-size: 19px;
    color: var(--ink-soft);
    white-space: nowrap;
  }
  .social-line .divider { color: var(--taupe); }

  /* Back */
  .card-back .monogram {
    position: absolute;
    left: 60px;
    top: 220px;
    font-size: 26px;
  }
  .card-back .identity {
    position: absolute;
    right: 50px;
    top: 56px;
    text-align: center;
  }
  .card-back .doctor-name { font-size: 40px; }
  .card-back .specialty { font-size: 19px; margin-top: 2px; }
  .contact-block {
    position: absolute;
    right: 50px;
    bottom: 44px;
    text-align: right;
    font-family: "Tinos", serif;
    font-style: normal;
    font-size: 23px;
    line-height: 1.38;
    color: var(--ink-soft);
    white-space: nowrap;
  }
</style>
</head>
<body>
  <main class="sheet">
    <section class="card card-front" aria-label="Frente do cartão">
      <div class="front-mark">
        <div class="monogram"><span class="monogram-dot"></span><span>Bastiani</span></div>
        <h1 class="doctor-name">DR. RENATO BASTIANI</h1>
        <p class="specialty">CIRURGIÃO PLÁSTICO</p>
      </div>
      <address class="social-line">
        <span>www.renatobastiani.med.br</span>
        <span class="divider">|</span>
        <span>fb.com/drrenatobastiani</span>
        <span class="divider">|</span>
        <span>@dr.renatobastiani</span>
      </address>
    </section>

    <section class="card card-back" aria-label="Verso do cartão">
      <div class="monogram"><span class="monogram-dot"></span><span>Bastiani</span></div>
      <div class="identity">
        <h2 class="doctor-name">DR. RENATO BASTIANI</h2>
        <p class="specialty">CIRURGIÃO PLÁSTICO</p>
      </div>
      <address class="contact-block">
        <p>CRM 507 219</p>
        <p>Av Dr Teixeira Lopes, 2710, sala 305</p>
        <p>Vila Olímpia | São Paulo/ SP - Phone: 11 4172-5036</p>
        <p>Al. Itapeva, 47, 3 andar</p>
        <p>Alphaville | Barueri/ SP - Phone: 11 6350-2481</p>
      </address>
    </section>
  </main>
</body>
</html>
```